US company marketing to law enforcement needs brochure design

We have created a new logo and now need to update our printed material. What we really need is a "style" or "template" for how our brochures will look in the future. Enclosed is the brochure draft with the old style and logo. Also enclosed is the new logo. As we are marketing to US law enforcement it is important the the brochure design is strong, powerful and that we are looking experienced and trustworthy. However, we also want to look modern in line with the logo update.

Target Market(s)

Law enforcement

Industry/Entity Type

Marketing

```html
<!DOCTYPE html>
<html lang="en">
<head>
<meta charset="utf-8">
<title>Keystone Alliance – Brochure Cover</title>
<link href="https://fonts.googleapis.com/css2?family=Merriweather:ital,wght@1,400&family=Open+Sans:ital,wght@0,600;1,400&display=swap" rel="stylesheet">
<style>
  :root {
    --navy: #1f3566;
    --paper: #ffffff;
    --backdrop: #e6e6e4;
    --name-grey: #a7a9ac;
    --list-grey: #6d6e71;
    --tick-grey: #b9bbbe;
    --fold: rgba(255,255,255,0.18);
  }
  * { margin: 0; padding: 0; box-sizing: border-box; }
  html, body {
    width: 1200px; height: 850px; overflow: hidden;
    background: var(--backdrop);
  }
  .brochure {
    position: absolute; left: 40px; top: 32px;
    width: 1120px; height: 786px;
    background: var(--paper);
    box-shadow: 0 2px 8px rgba(0,0,0,0.18);
    overflow: hidden;
  }
  .cover-art { position: absolute; inset: 0; width: 1120px; height: 786px; }
  .brand {
    position: absolute; display: flex; align-items: center;
    font-family: "Open Sans", sans-serif; font-weight: 600;
    letter-spacing: -0.5px; white-space: nowrap;
  }
  .brand__dot { border-radius: 50%; flex: none; }
  .brand--front { left: 602px; top: 29px; font-size: 40px; color: var(--name-grey); gap: 16px; }
  .brand--front .brand__dot { width: 64px; height: 64px; background: var(--paper); }
  .brand--back { left: 98px; top: 692px; font-size: 33px; color: var(--navy); gap: 14px; }
  .brand--back .brand__dot { width: 60px; height: 60px; background: var(--navy); }
  .headline {
    position: absolute; right: 63px; top: 596px;
    font-family: "Merriweather", serif; font-style: italic; font-weight: 400;
    font-size: 25px; color: var(--navy); white-space: nowrap;
  }
  .program-list {
    position: absolute; left: 600px; width: 476px;
    display: flex; justify-content: center; gap: 14px;
    font-family: "Open Sans", sans-serif; font-style: italic;
    font-size: 18.5px; color: var(--list-grey); list-style: none; white-space: nowrap;
  }
  .program-list--first { top: 668px; }
  .program-list--second { top: 711px; }
  .program-list li { display: flex; align-items: center; gap: 5px; }
  .tick { width: 20px; height: 20px; flex: none; }
</style>
</head>
<body>
  <main class="brochure">
    <svg class="cover-art" viewBox="0 0 1120 786" xmlns="http://www.w3.org/2000/svg">
      <defs>
        <linearGradient id="photo-tone" x1="0" y1="0" x2="1" y2="1">
          <stop offset="0" stop-color="#6b3a1c"/>
          <stop offset="0.35" stop-color="#c8692a"/>
          <stop offset="0.6" stop-color="#b8561e"/>
          <stop offset="0.85" stop-color="#e2b36a"/>
          <stop offset="1" stop-color="#5a3218"/>
        </linearGradient>
      </defs>
      <rect class="navy-field" x="0" y="0" width="1120" height="455" fill="var(--navy)"/>
      <rect class="rule" x="0" y="462" width="1120" height="7" fill="var(--navy)"/>
      <rect class="foot-rule" x="0" y="782" width="1120" height="4" fill="var(--navy)"/>
      <polygon class="photo-area" role="img"
        aria-label="Photograph of a wooden judge's gavel and brass scales of justice on a warm amber background"
        points="349,129 1077,129 953,534 243,534" fill="url(#photo-tone)"/>
      <polygon points="349,129 420,129 300,534 243,534" fill="rgba(255,255,255,0.12)"/>
      <polygon points="1010,129 1077,129 953,534 900,534" fill="rgba(31,53,102,0.25)"/>
      <line class="fold" x1="560" y1="0" x2="560" y2="786" stroke="var(--fold)" stroke-width="1"/>
    </svg>

    <div class="brand brand--front"><span class="brand__dot"></span>Keystone Alliance</div>

    <h1 class="headline">Comprehensive Offender Programs</h1>

    <ul class="program-list program-list--first">
      <li><svg class="tick" viewBox="0 0 20 20"><path d="M3 11 L8 16 L18 3" fill="none" stroke="var(--tick-grey)" stroke-width="2"/></svg>Pre Trial</li>
      <li><svg class="tick" viewBox="0 0 20 20"><path d="M3 11 L8 16 L18 3" fill="none" stroke="var(--tick-grey)" stroke-width="2"/></svg>Diversion</li>
      <li><svg class="tick" viewBox="0 0 20 20"><path d="M3 11 L8 16 L18 3" fill="none" stroke="var(--tick-grey)" stroke-width="2"/></svg>Deferred Prosecution</li>
    </ul>
    <ul class="program-list program-list--second">
      <li><svg class="tick" viewBox="0 0 20 20"><path d="M3 11 L8 16 L18 3" fill="none" stroke="var(--tick-grey)" stroke-width="2"/></svg>Jail Alternative</li>
      <li><svg class="tick" viewBox="0 0 20 20"><path d="M3 11 L8 16 L18 3" fill="none" stroke="var(--tick-grey)" stroke-width="2"/></svg>Probation</li>
    </ul>

    <div class="brand brand--back"><span class="brand__dot"></span>Keystone Alliance</div>
  </main>
</body>
</html>
```